Business Card

We need a business card for a fundraising/sales and marketing company called Kelvora Appeals services. The logo colours are Red Black and white. The final design should communicate professional, reliable yet fun and charity minded
Updates

Sorry for the delay. A decision will be made in the next 48 hours. we are stuck between two designs. Kind Regards, Molly Ravenscroft

Industry/Entity Type

Marketing

```html
<!DOCTYPE html>
<html lang="en">
<head>
<meta charset="utf-8">
<title>Kelvora Appeals services – Business Card</title>
<link rel="stylesheet" href="https://fonts.googleapis.com/css2?family=Arimo:wght@400;700&display=swap">
<style>
  :root {
    --brand-red: #c01f2a;
    --ink: #2b2b2b;
    --ink-soft: #444444;
    --paper: #ffffff;
    --backdrop: #ebe8e4;
  }
  * { box-sizing: border-box; margin: 0; padding: 0; }
  html, body {
    width: 1200px;
    height: 721px;
    overflow: hidden;
  }
  body {
    background: var(--backdrop);
    font-family: "Arimo", Arial, sans-serif;
    color: var(--ink);
    position: relative;
  }
  .business-card {
    position: absolute;
    left: 150px;
    top: 103px;
    width: 900px;
    height: 514px;
    background: var(--paper);
    box-shadow: 0 8px 24px rgba(0,0,0,0.18);
    overflow: hidden;
  }
  .band-top {
    position: absolute;
    left: 0; top: 0;
    width: 100%;
    height: 84px;
    background: var(--brand-red);
  }
  .band-bottom {
    position: absolute;
    left: 0; bottom: 0;
    width: 100%;
    height: 132px;
    background: var(--brand-red);
  }
  .website {
    position: absolute;
    left: 0; right: 0;
    top: 28px;
    padding-left: 240px;
    text-align: center;
    color: var(--paper);
    font-size: 22px;
    letter-spacing: 4px;
  }
  .brand {
    position: absolute;
    left: 92px;
    top: 226px;
    display: flex;
    align-items: center;
    gap: 14px;
  }
  .brand-mark {
    width: 26px;
    height: 26px;
    background: var(--brand-red);
  }
  .brand-name {
    font-size: 38px;
    font-weight: 700;
    color: var(--brand-red);
    letter-spacing: 1px;
  }
  .contact-block {
    position: absolute;
    left: 560px;
    top: 126px;
  }
  .person-name {
    font-size: 30px;
    font-weight: 400;
    color: var(--ink);
    line-height: 1;
  }
  .person-title {
    font-size: 17px;
    color: var(--brand-red);
    margin-top: 4px;
  }
  .contact-list {
    list-style: none;
    margin-top: 18px;
  }
  .contact-list li {
    display: flex;
    align-items: center;
    gap: 12px;
    font-size: 19px;
    color: var(--ink-soft);
    line-height: 27px;
  }
  .contact-icon {
    width: 18px;
    height: 18px;
    flex: none;
  }
  .contact-icon path, .contact-icon rect {
    fill: var(--brand-red);
  }
</style>
</head>
<body>
  <article class="business-card">
    <div class="band-top"></div>

    <div class="brand">
      <span class="brand-mark"></span>
      <span class="brand-name">Kelvora Appeals</span>
    </div>

    <section class="contact-block">
      <h1 class="person-name">YOUR NAME</h1>
      <p class="person-title">President</p>
      <ul class="contact-list">
        <li>
          <svg class="contact-icon" viewBox="0 0 18 18" aria-hidden="true"><path d="M9 1 L17 8 H14.5 V17 H11 V12 H7 V17 H3.5 V8 H1 Z"/></svg>
          Street No. 23 British
        </li>
        <li>
          <svg class="contact-icon" viewBox="0 0 18 18" aria-hidden="true"><path d="M5 1 H13 A1.5 1.5 0 0 1 14.5 2.5 V15.5 A1.5 1.5 0 0 1 13 17 H5 A1.5 1.5 0 0 1 3.5 15.5 V2.5 A1.5 1.5 0 0 1 5 1 Z M5.5 3 V13 H12.5 V3 Z"/></svg>
          + 123.456.789
        </li>
        <li>
          <svg class="contact-icon" viewBox="0 0 18 18" aria-hidden="true"><path d="M4 1.5 L7 1.5 L8.5 5.5 L6.5 7 C7.5 9 9 10.5 11 11.5 L12.5 9.5 L16.5 11 V14 C16.5 15.5 15 16.5 13.5 16.5 C7 16 2 11 1.5 4.5 C1.5 3 2.5 1.5 4 1.5 Z"/></svg>
          + 123.456.789
        </li>
        <li>
          <svg class="contact-icon" viewBox="0 0 18 18" aria-hidden="true"><path d="M1 4 H17 V14 H1 Z M2.5 5.2 L9 10 L15.5 5.2 Z" fill-rule="evenodd"/></svg>
          username@companyname.com
        </li>
      </ul>
    </section>

    <footer class="band-bottom">
      <p class="website">www.companyname.com</p>
    </footer>
  </article>
</body>
</html>
```